Business Card Design for a technology company

Our current business card is outdated and stale.

We need a new look and one soon.

We're a telematics (GPS tracking) company based in Australia. Our audiences are transport and logistics company.

Target Market(s)

1. Transport and Logistics Companies
2. Food and Beverage Manufacturers
3. Concrete Businesses

Industry/Entity Type

Logistics

Contact Information for Business Card

Halvor Pinet

Font styles to use
Sans Serif

Colors
3276b5
0255a3
85acd3
cfdeed
ffffff

Requirements
Must have
• Logo
• "Premium Suppliers of Real Time Temperature Tracking"
• Contact Name
• Business Title
• Address
• Telephone
• Mobile
• Email
• Website URL
Nice to have
• Visual representation of tracking or maps.
Should not have
• Image of a satellite as currently shown

```html
<!DOCTYPE html>
<html lang="en">
<head>
<meta charset="utf-8">
<title>Halvor Pinet – Business Card</title>
<link rel="stylesheet" href="https://fonts.googleapis.com/css2?family=Open+Sans:wght@400;600;700&display=swap">
<style>
  :root {
    --backdrop: #3a3a3a;
    --card-light: #ececec;
    --brand-blue: #0255a3;
    --name-blue: #3276b5;
    --sky-top: #6aa3dc;
    --sky-bottom: #3a72c2;
    --night: #1c1c1e;
    --ink: #1a1a1a;
    --ink-soft: #4a4a4a;
    --rule: #9a9a9a;
    --navy: #0a2a78;
    --white: #ffffff;
  }
  * { margin: 0; padding: 0; box-sizing: border-box; }
  html, body { width: 1200px; height: 900px; overflow: hidden; }
  body {
    background: var(--backdrop);
    font-family: "Open Sans", Arial, sans-serif;
    position: relative;
  }
  .card {
    position: absolute;
    top: 170px;
    width: 347px;
    height: 561px;
    box-shadow: 2px 3px 6px rgba(0,0,0,0.45);
    overflow: hidden;
  }
  .card--front { left: 259px; background: var(--card-light); text-align: center; }
  .card--back {
    left: 631px;
    background: linear-gradient(180deg, var(--sky-top) 0%, var(--sky-bottom) 100%);
  }

  /* Front */
  .brand {
    position: absolute;
    top: 132px;
    left: 0; right: 0;
    font-size: 38px;
    font-weight: 600;
    color: var(--brand-blue);
    letter-spacing: -0.5px;
    line-height: 1;
  }
  .tagline {
    position: absolute;
    top: 193px;
    left: 0; right: 0;
    font-size: 12px;
    line-height: 17px;
    color: var(--ink);
    text-transform: uppercase;
    letter-spacing: 0.2px;
  }
  .person { position: absolute; top: 324px; left: 0; right: 0; }
  .person__name { font-size: 23px; color: var(--name-blue); line-height: 26px; }
  .person__role { font-size: 15px; color: var(--ink-soft); line-height: 20px; }
  .rule {
    position: absolute;
    left: 92px;
    width: 163px;
    height: 1px;
    background: var(--rule);
  }
  .rule--top { top: 376px; }
  .rule--bottom { top: 473px; }
  .contact {
    position: absolute;
    top: 385px;
    left: 0; right: 0;
    font-size: 15px;
    line-height: 20px;
    color: var(--ink-soft);
    list-style: none;
  }
  .contact__label { color: var(--navy); font-weight: 700; }
  .contact__web { color: var(--navy); font-weight: 700; }
  .address {
    position: absolute;
    top: 483px;
    left: 0; right: 0;
    font-size: 15px;
    line-height: 21px;
    color: var(--ink-soft);
    font-style: normal;
  }

  /* Back */
  .back__lower {
    position: absolute;
    left: 0; right: 0; bottom: 0;
    height: 308px;
    background: var(--night);
  }
  .back__disc {
    position: absolute;
    top: 57px;
    left: 103px;
    width: 140px;
    height: 140px;
    border-radius: 50%;
    background: var(--white);
  }
  .back__brand {
    position: absolute;
    top: 376px;
    left: 0; right: 0;
    text-align: center;
    font-size: 40px;
    font-weight: 600;
    line-height: 1;
    color: var(--white);
    letter-spacing: -0.5px;
  }
</style>
</head>
<body>
  <section class="card card--front">
    <div class="brand">Halvor Pinet</div>
    <p class="tagline">Premium suppliers of real time<br>temperature tracking</p>
    <div class="person">
      <p class="person__name">Maren Ellery</p>
      <p class="person__role">Managing Director</p>
    </div>
    <div class="rule rule--top"></div>
    <ul class="contact">
      <li><span class="contact__label">P:</span> 044-987 654 321</li>
      <li><span class="contact__label">M:</span> 044-987 654 321</li>
      <li><span class="contact__label">E:</span> hello@halvorpinet.com</li>
      <li class="contact__web">www.halvorpinet.com</li>
    </ul>
    <div class="rule rule--bottom"></div>
    <address class="address">48 Harbourline Road<br>Fremantle WA, 6160.</address>
  </section>

  <section class="card card--back">
    <div class="back__disc"></div>
    <div class="back__lower"></div>
    <div class="back__brand">Halvor Pinet</div>
  </section>
</body>
</html>
```